Stonelynk Business Card Design

The Stonelynk Co is an aggregate (crushing) equipment dealer serving Western Canadian provinces. Stonelynk is a distributor of aggregate equipment for different manufacturers.

We are looking to change and update the existing business card which has been used since the existence of the company. A copy of existing card has been attached for reference. The Stonelynk Co logo we want to remain the same and we want the green color to remain the same.

We are wanting something new with a different look. A refreshing card to show a new modern and updated look. No longer wanting to have the manufacturers on the back of the card but something more like our logo on the back of the card with a statement like "Crushing Solutions"

ideas could be:
- card can be different colors on front and back
- front or reverse of the card could possibly be the green color with the logo in black

Target Market(s)

Owners of Aggregate/Crushing companies

Requirements
Must have
• - logo to remain same along with same font within logo
• - green color to remain same
Nice to have
• as noted above under project description
Should not have

```html
<!DOCTYPE html>
<html lang="en">
<head>
<meta charset="utf-8">
<title>Stonelynk Business Card</title>
<link href="https://fonts.googleapis.com/css2?family=Arimo:wght@400;700&display=swap" rel="stylesheet">
<style>
  :root {
    --backdrop: #1b1b1b;
    --paper: #ffffff;
    --brand-green: #8b8c08;
    --brand-green-light: #9c9c2e;
    --ink: #1a1a1a;
    --rule: #9a9a9a;
  }
  * { margin: 0; padding: 0; box-sizing: border-box; }
  html, body { width: 1200px; height: 900px; overflow: hidden; }
  body {
    position: relative;
    background: var(--backdrop);
    font-family: "Arimo", Arial, sans-serif;
    color: var(--ink);
  }
  .card {
    position: absolute;
    top: 170px;
    width: 347px;
    height: 561px;
    box-shadow: 3px 3px 6px rgba(0,0,0,0.6);
    overflow: hidden;
  }
  .card--front { left: 259px; background: var(--paper); text-align: center; }
  .card--back { left: 631px; background: var(--brand-green); }

  .brand-mark {
    position: absolute;
    left: 50%;
    top: 110px;
    width: 30px;
    height: 30px;
    margin-left: -15px;
    border-radius: 50%;
    background: var(--brand-green);
  }
  .brand-name {
    position: absolute;
    left: 0; right: 0;
    top: 182px;
    font-size: 27px;
    font-weight: 700;
    letter-spacing: 0.6px;
    color: var(--ink);
  }
  .holder-name {
    position: absolute;
    left: 0; right: 0;
    top: 314px;
    font-size: 21px;
    font-weight: 400;
    color: var(--brand-green);
    letter-spacing: 0.3px;
  }
  .divider {
    position: absolute;
    left: 83px;
    width: 181px;
    height: 1px;
    background: var(--rule);
  }
  .divider--top { top: 349px; }
  .divider--bottom { top: 411px; }
  .address {
    position: absolute;
    left: 0; right: 0;
    top: 360px;
    font-size: 15.5px;
    line-height: 20px;
    font-style: normal;
  }
  .contact {
    position: absolute;
    left: 0; right: 0;
    top: 423px;
    font-size: 15.5px;
    line-height: 20.3px;
    list-style: none;
  }
  .contact .label { color: var(--brand-green); font-weight: 700; }
  .contact .web { color: var(--brand-green); }

  .back-field {
    position: absolute;
    inset: 0;
    background: linear-gradient(180deg,
      var(--brand-green-light) 0%,
      var(--brand-green) 40%,
      var(--brand-green) 75%,
      var(--brand-green-light) 100%);
  }
  .back-name {
    position: absolute;
    left: 0; right: 0;
    top: 256px;
    text-align: center;
    font-size: 34px;
    font-weight: 700;
    letter-spacing: 1px;
    color: var(--paper);
  }
  .tagline {
    position: absolute;
    left: 0; right: 0;
    top: 470px;
    text-align: center;
    font-size: 16.5px;
    font-weight: 700;
    letter-spacing: 1.6px;
    color: var(--paper);
  }
</style>
</head>
<body>
  <section class="card card--front">
    <span class="brand-mark"></span>
    <h1 class="brand-name">THE STONELYNK CO.</h1>
    <h2 class="holder-name">DEREK HOLLAN</h2>
    <div class="divider divider--top"></div>
    <address class="address">2210-48B Avenue<br>Nisku, Alberta T9E 1K2</address>
    <div class="divider divider--bottom"></div>
    <ul class="contact">
      <li><span class="label">P:</span> 780.555.0142(Direct)</li>
      <li><span class="label">P:</span> 780.555.0187</li>
      <li><span class="label">F:</span> 780.555.0193</li>
      <li><span class="label">E:</span> derek@stonelynk.com</li>
      <li class="web">www.stonelynk.ca</li>
    </ul>
  </section>

  <section class="card card--back">
    <div class="back-field" role="img" aria-label="Decorative background of layered wave bands in two tones of green"></div>
    <div class="back-name">STONELYNK</div>
    <p class="tagline">CRUSHING SOLUTIONS</p>
  </section>
</body>
</html>
```